Envelope Design for Regional Saddleborne Heritage Trust--Museum outside Camp Brellin Texas

Design a 9"x12" carrier (flat ENVELOPE) for Museum test mailing that incorporates 11 cavalry or armor unit patches, as well as teaser copy about Gen. Calloway and info on the signer LTG Driscoe.
Upper left (or center w/faux label) 3 star army flag (find online) Lieutenant General Mark T. Driscoe, US Army (Retired)
Teaser handwritten bigger: Inside: Meet General Calloway
11 unit patches plus RSHT logo. This is a closed faced envelope.

Project Deadline Extended Reason: I thought I submitted things on Monday but didn't. Also, didn't guarantee which reduces number of entries. Added Thursday, April 7, 2016

Target Market(s)

Military veterans, people who like the army, Vietnam Veterans, older men, Texans

Industry/Entity Type

Museum

Font styles to use
Other font styles liked:
• I will leave this to you. I probably would do the Calloway teaser in handwritten font to stand out.

Requirements
Must have
• Upper left (or in center as part of a faux label) should have LTG's name an 3 star army flag which can be found online
• handwritten teaser about Gen Calloway
• 11 unit patches -- you can include logo if you like. I've mailed calendars in flats many times and sometimes put a faux label in center that looks good. Logo could go here but doesn't have to. LTG flag is probably more impressive
• Address: 482 North Lorimer Row
• Killeen, Texas 70953
Nice to have
• If you go with a faux label (not pushing this idea), it's good to have enough contrast that it looks like an actual label from distance. I'm not sure if it's best to display the 11 patches in a circle or diagonally. I'm a writer not a designer.

```html
<!DOCTYPE html>
<html lang="en">
<head>
<meta charset="utf-8">
<title>Regional Saddleborne Heritage Trust – Carrier Envelope</title>
<link rel="stylesheet" href="https://fonts.googleapis.com/css2?family=Archivo:ital,wght@0,400;0,700;1,800&family=Parisienne&family=Roboto+Slab:wght@400;800&display=swap">
<style>
  :root {
    --frame-navy: #1c4a70;
    --ink-navy: #12306b;
    --label-red: #d7141f;
    --teaser-red: #e01b24;
    --shadow-grey: #6d6d6d;
    --paper: #ffffff;
    --ink: #111111;
    --patch-ring: #e8242c;
    --patch-blue-ring: #2da6e8;
  }
  * { margin: 0; padding: 0; box-sizing: border-box; }
  html, body { width: 1200px; height: 905px; overflow: hidden; background: var(--paper); }
  .envelope {
    position: relative;
    width: 1200px;
    height: 905px;
    background: var(--paper);
    border: 14px solid var(--frame-navy);
    font-family: "Archivo", Arial, sans-serif;
  }
  .signer-label { position: absolute; left: 0; top: 0; }
  .signer-rank { font-family: "Roboto Slab", Georgia, serif; font-weight: 400; font-size: 22px; fill: var(--ink); }
  .signer-name { font-family: "Roboto Slab", Georgia, serif; font-weight: 800; font-size: 40px; fill: var(--ink); }
  .signer-service { font-family: "Roboto Slab", Georgia, serif; font-weight: 400; font-size: 23px; fill: var(--ink); }

  .teaser {
    position: absolute;
    left: 0; right: 0; top: 360px;
    text-align: center;
  }
  .teaser-kicker {
    font-weight: 800; font-style: italic;
    font-size: 27px; letter-spacing: 1px;
    color: var(--ink-navy);
  }
  .teaser-headline {
    font-family: "Parisienne", cursive;
    font-weight: 400;
    font-size: 88px; line-height: 1.05;
    color: var(--teaser-red);
    margin-top: -2px;
  }
  .trust-name {
    display: flex; align-items: center; justify-content: center; gap: 12px;
    margin-top: 22px;
    font-weight: 700; font-size: 23px; letter-spacing: 0.5px;
    color: var(--ink-navy);
    text-transform: uppercase;
  }
  .trust-name .mark { width: 18px; height: 18px; border-radius: 50%; background: var(--ink-navy); }

  .return-address { position: absolute; left: 42px; top: 728px; }
  .address-heading {
    font-weight: 800; font-style: italic;
    font-size: 29px; letter-spacing: 0.5px;
    color: var(--ink-navy);
    margin-bottom: 14px;
  }
  .address-line { font-size: 20px; line-height: 34px; color: var(--ink); text-transform: uppercase; }

  .unit-patches { position: absolute; left: 0; top: 0; }
</style>
</head>
<body>
<div class="envelope">

  <svg class="signer-label" width="1172" height="877" viewBox="14 14 1172 877" aria-label="Lieutenant General Mark T. Driscoe, US Army (Retired)">
    <defs>
      <clipPath id="paper-area"><rect x="14" y="14" width="1172" height="877"/></clipPath>
    </defs>
    <g clip-path="url(#paper-area)">
      <g transform="translate(66 366) rotate(-45)">
        <rect x="0" y="-240" width="413" height="240" rx="10" fill="var(--shadow-grey)"/>
      </g>
      <g transform="translate(56 356) rotate(-45)">
        <rect x="0" y="-240" width="413" height="240" rx="10" fill="var(--label-red)"/>
      </g>
      <g fill="#ffffff">
        <polygon points="84,36 88,48 101,48 91,56 95,69 84,61 73,69 77,56 67,48 80,48"/>
        <polygon points="126,24 130,36 143,36 133,44 137,57 126,49 115,57 119,44 109,36 122,36"/>
        <polygon points="62,94 66,106 79,106 69,114 73,127 62,119 51,127 55,114 45,106 58,106"/>
      </g>
      <g transform="translate(152 182) rotate(-45)" text-anchor="middle">
        <text class="signer-rank" x="4" y="-42">Lieutenant General</text>
        <text class="signer-name" x="0" y="8">Mark T. Driscoe</text>
        <text class="signer-service" x="4" y="44">US Army (Retired)</text>
      </g>
    </g>
  </svg>

  <div class="teaser">
    <div class="teaser-kicker">INSIDE:</div>
    <div class="teaser-headline">Meet General Calloway</div>
    <div class="trust-name"><span class="mark"></span>Regional Saddleborne Heritage Trust</div>
  </div>

  <div class="return-address">
    <div class="address-heading">ADDRESS:</div>
    <div class="address-line">482 North Lorimer Row</div>
    <div class="address-line">Killeen, Texas 70953</div>
  </div>

  <svg class="unit-patches" width="1172" height="877" viewBox="14 14 1172 877">
    <g role="img" aria-label="Regional command unit patch">
      <circle cx="694" cy="754" r="44" fill="var(--patch-blue-ring)"/>
      <circle cx="694" cy="754" r="39" fill="#ffffff"/>
      <circle cx="694" cy="754" r="34" fill="#4a8fd0"/>
    </g>
    <g role="img" aria-label="Aviation brigade unit patch">
      <circle cx="783" cy="711" r="37" fill="var(--patch-ring)"/><circle cx="783" cy="711" r="32" fill="#fff"/><circle cx="783" cy="711" r="28" fill="#c8552e"/>
    </g>
    <g role="img" aria-label="Corps support unit patch">
      <circle cx="861" cy="711" r="37" fill="var(--patch-ring)"/><circle cx="861" cy="711" r="32" fill="#fff"/><circle cx="861" cy="711" r="28" fill="#3a62a8"/>
    </g>
    <g role="img" aria-label="Infantry division unit patch">
      <circle cx="939" cy="711" r="37" fill="var(--patch-ring)"/><circle cx="939" cy="711" r="32" fill="#fff"/><circle cx="939" cy="711" r="28" fill="#3f8a3a"/>
    </g>
    <g role="img" aria-label="Cavalry division unit patch">
      <circle cx="1017" cy="711" r="37" fill="var(--patch-ring)"/><circle cx="1017" cy="711" r="32" fill="#fff"/><circle cx="1017" cy="711" r="28" fill="#e3c21f"/>
    </g>
    <g role="img" aria-label="Cavalry regiment unit patch">
      <circle cx="1095" cy="711" r="37" fill="var(--patch-ring)"/><circle cx="1095" cy="711" r="32" fill="#fff"/><circle cx="1095" cy="711" r="28" fill="#2f5a2c"/>
    </g>
    <g role="img" aria-label="Armored division unit patch">
      <circle cx="783" cy="789" r="37" fill="var(--patch-ring)"/><circle cx="783" cy="789" r="32" fill="#fff"/><circle cx="783" cy="789" r="28" fill="#d8a21e"/>
    </g>
    <g role="img" aria-label="Armored division unit patch">
      <circle cx="861" cy="789" r="37" fill="var(--patch-ring)"/><circle cx="861" cy="789" r="32" fill="#fff"/><circle cx="861" cy="789" r="28" fill="#e0821e"/>
    </g>
    <g role="img" aria-label="Tank battalion unit patch">
      <circle cx="939" cy="789" r="37" fill="var(--patch-ring)"/><circle cx="939" cy="789" r="32" fill="#fff"/><circle cx="939" cy="789" r="28" fill="#d9d9d9"/>
    </g>
    <g role="img" aria-label="Armored division unit patch">
      <circle cx="1017" cy="789" r="37" fill="var(--patch-ring)"/><circle cx="1017" cy="789" r="32" fill="#fff"/><circle cx="1017" cy="789" r="28" fill="#e0821e"/>
    </g>
    <g role="img" aria-label="Army corps unit patch">
      <circle cx="1095" cy="789" r="37" fill="var(--patch-ring)"/><circle cx="1095" cy="789" r="32" fill="#fff"/><circle cx="1095" cy="789" r="28" fill="#4a4fa8"/>
    </g>
  </svg>

</div>
</body>
</html>
```